Management Consulting firm needs business model Infographic

Thornwell Partners is a diversity and inclusion consulting firm. We engage in strategy development, knowledge transfer, and coaching. Our primary colors are red (f02e25), black (241e20), grey (c7c8ca) and white (ffffff) that can be highlighted with (ED7F21), (158A8F) and (1ABB24).

We are looking for a graphical representation of the Thornwell Partners business model. We describe what we do as addressing Diversity & Inclusion challenges and opportunities through Relevant Knowledge, Customized Strategies and Measurable Results. Our tagline is: D&I Models, Assessments and Tools for You!

We believe our business model has three stages or phases.
1. Diversity & Inclusion business challenges or opportunities arise such as changing demographics, lost market share, declining revenue, stalled innovation, attracting and retaining top talent, next-generation leadership development, abusive behavior in the workplace, etc.
2. These challenges or opportunities motivate an organization to re-examine the work culture their behaviors create, particularly the mindset, knowledge set and skillset of organizational executives
3. We develop models, assessments and tools that determine and leverage what the organization has been culturally and identify the strategies, action plans, and metrics it needs to address that business challenge or seize those business opportunity.
Thus a client can expect Thornwell Partners to generate Relevant Knowledge, Customized Strategies and Measurable Results.

The designer can visit our website https://www.thornwellpartners-example.com/ , and read a blog post https://www.thornwellpartners-example.com/blog-news-cultural-diversity/leading-inclusively-how-cultural-competence-aids-performance for background.

The ideal infographic is one where a portion of it (or in totality) can be used as a Chatterbox, Workmesh and Peeplet profile banner.

We have includes some sample infographics that we like.
1) The first is within a PowerPoint deck, Slide 1 is the original infographic template and slide 2 is an example of how TP business model could be added.
2) The other three are also styles we like.

Target Market(s)

Business executives

Industry/Entity Type

Management Consulting

Font styles to use
Sans Serif
Other font styles liked:
• Lato

Colors
ec1f27
000000
474747
0392cd
00a990
9bcb3b

Requirements
Must have
• We are looking for a graphical representation of the Thornwell Partners business model. The design must the four components describing what we do: 1) An organization facing a Diversity & Inclusion challenge or opportunity. We address that challenge or opportunity through 2) Relevant Knowledge, 3) Customized Strategies and 4) Measurable Results.
• The design must include the tagline: D&I Models, Assessments and Tools for You!
• We prefer a horizontal / landscape.
Nice to have
• A nice to have is if the design (either in whole, or part) can be used on Chatterbox, Peeplet or Workmesh profile banners
• Another nice to have is if the business challenges/opportunities component of the infographic includes examples such as changing demographics, lost market share, declining revenue, stalled innovation, attracting and retaining top talent, next-generation leadership development, abusive behavior in the workplace, etc.
• A nice to have is if the design (either in whole, or part) can be used on the back of a business a card
Should not have
• Silly, unprofessional or business pictures, or icons.

```html
<!DOCTYPE html>
<html lang="en">
<head>
<meta charset="utf-8">
<title>Thornwell Partners – Embrace Changing Demographics</title>
<link rel="stylesheet" href="https://fonts.googleapis.com/css2?family=Barlow:wght@500;600&family=Barlow+Condensed:wght@500;600;700&family=Barlow+Semi+Condensed:wght@500;600&display=swap">
<style>
  :root {
    --red: #ee3348;
    --black: #111111;
    --ink: #241e20;
    --grey: #6b6b6b;
    --orange: #f28c28;
    --teal: #1fb3ba;
    --green: #97c23d;
    --white: #ffffff;
  }
  html, body {
    margin: 0;
    padding: 0;
    width: 1200px;
    height: 927px;
    overflow: hidden;
    background: var(--white);
  }
  .infographic {
    position: relative;
    width: 1200px;
    height: 927px;
    font-family: "Barlow Condensed", "Arial Narrow", sans-serif;
  }
  .model-diagram {
    position: absolute;
    left: 0;
    top: 0;
  }
  .pillar-title {
    font-family: "Barlow Semi Condensed", "Arial Narrow", sans-serif;
    font-weight: 500;
    font-size: 25px;
  }
  .pillar-item {
    font-family: "Barlow Semi Condensed", "Arial Narrow", sans-serif;
    font-weight: 500;
    font-size: 15.5px;
  }
  .hub-label {
    font-family: "Barlow", Arial, sans-serif;
    font-weight: 600;
    font-size: 17px;
  }
  .brand {
    position: absolute;
    left: 838px;
    top: 138px;
    display: flex;
    align-items: center;
    gap: 12px;
  }
  .brand-dot {
    width: 16px;
    height: 16px;
    border-radius: 50%;
    background: var(--red);
  }
  .brand-name {
    font-family: "Barlow Condensed", "Arial Narrow", sans-serif;
    font-weight: 700;
    font-size: 44px;
    line-height: 40px;
    color: var(--ink);
    margin: 0;
  }
  .divider {
    position: absolute;
    left: 536px;
    top: 347px;
    width: 7px;
    height: 234px;
    background: var(--black);
  }
  .headline {
    position: absolute;
    left: 590px;
    top: 338px;
    margin: 0;
    white-space: nowrap;
    font-family: "Barlow Condensed", "Arial Narrow", sans-serif;
    font-weight: 700;
    font-size: 86px;
    line-height: 64px;
    color: var(--red);
    text-transform: uppercase;
    transform: scaleX(0.83);
    transform-origin: left top;
  }
  .stage-label {
    position: absolute;
    top: 504px;
    margin: 0;
    font-family: "Barlow", Arial, sans-serif;
    font-weight: 500;
    font-size: 20px;
    line-height: 23px;
    letter-spacing: 0.6px;
    color: var(--white);
  }
  .stage-knowledge { left: 591px; }
  .stage-strategies { left: 796px; }
  .stage-results { left: 993px; }
  .tagline {
    position: absolute;
    left: 591px;
    top: 586px;
    margin: 0;
    font-family: "Barlow", Arial, sans-serif;
    font-weight: 500;
    font-size: 20px;
    line-height: 24px;
    color: var(--grey);
  }
</style>
</head>
<body>
<main class="infographic">

  <svg class="model-diagram" width="1200" height="927" viewBox="0 0 1200 927" aria-label="Business model: workplace, marketplace and community around challenges and opportunities">
    <path class="connector-workplace" fill="var(--orange)" d="M345,330 C362,360 366,385 358,410 L412,410 C404,385 408,360 425,330 Z"/>
    <path class="connector-marketplace" fill="var(--teal)" d="M250,420 C285,438 300,440 330,440 L330,490 C300,490 285,492 250,510 Z"/>
    <path class="connector-community" fill="var(--green)" d="M358,520 C366,545 362,570 345,600 L425,600 C408,570 404,545 412,520 Z"/>

    <circle cx="380" cy="245" r="108" fill="none" stroke="var(--orange)" stroke-width="1.5"/>
    <circle cx="380" cy="245" r="96" fill="var(--orange)"/>
    <g fill="var(--white)">
      <text class="pillar-title" x="305" y="229">WORKPLACE:</text>
      <text class="pillar-item" x="317" y="250">• Diversify Talent</text>
      <text class="pillar-item" x="317" y="272">• Increase Engagement</text>
      <text class="pillar-item" x="317" y="293">• Improve Performance</text>
    </g>

    <circle cx="168" cy="456" r="108" fill="none" stroke="var(--teal)" stroke-width="1.5"/>
    <circle cx="168" cy="456" r="96" fill="var(--teal)"/>
    <g fill="var(--white)">
      <text class="pillar-title" x="94" y="436">MARKETPLACE:</text>
      <text class="pillar-item" x="117" y="457">• Gain Market Share</text>
      <text class="pillar-item" x="117" y="478">• Grow Revenue</text>
      <text class="pillar-item" x="117" y="499">• Improve Innovation</text>
    </g>

    <circle cx="385" cy="668" r="108" fill="none" stroke="var(--green)" stroke-width="1.5"/>
    <circle cx="385" cy="668" r="96" fill="var(--green)"/>
    <g fill="var(--white)">
      <text class="pillar-title" x="322" y="655">COMMUNITY:</text>
      <text class="pillar-item" x="322" y="675">• Foster Sustainability</text>
      <text class="pillar-item" x="322" y="696">• Establish Partnerships</text>
      <text class="pillar-item" x="322" y="717">• Generate Advocacy</text>
    </g>

    <circle cx="385" cy="465" r="74" fill="var(--white)"/>
    <path class="hub-ring" fill="none" stroke="var(--red)" stroke-width="11" d="M437,424 A66,66 0 1 0 444,495"/>
    <polygon fill="var(--red)" points="452,440 420,426 448,410"/>
    <path fill="none" stroke="var(--orange)" stroke-width="8" d="M350,447 A40,40 0 0 1 410,433"/>
    <polygon fill="var(--orange)" points="420,440 402,424 412,446"/>
    <path fill="none" stroke="var(--teal)" stroke-width="8" d="M352,495 A40,40 0 0 1 346,458"/>
    <path fill="none" stroke="var(--green)" stroke-width="8" d="M420,488 A40,40 0 0 1 362,502"/>
    <g fill="var(--red)">
      <text class="hub-label" x="374" y="466">CHALLENGES &amp;</text>
      <text class="hub-label" x="374" y="487">OPPORTUNITIES</text>
    </g>

    <g fill="var(--black)">
      <polygon points="543,488 736,488 766,523 736,558 543,558"/>
      <polygon points="746,488 932,488 962,523 932,558 746,558 776,523"/>
      <polygon points="942,488 1115,488 1145,523 1115,558 942,558 972,523"/>
    </g>
  </svg>

  <div class="brand">
    <span class="brand-dot"></span>
    <p class="brand-name">Thornwell<br>Partners</p>
  </div>

  <div class="divider"></div>

  <h1 class="headline">Embrace Changing<br>Demographics</h1>

  <p class="stage-label stage-knowledge">Relevant<br>Knowledge</p>
  <p class="stage-label stage-strategies">Customized<br>Strategies</p>
  <p class="stage-label stage-results">Measurable<br>Results</p>

  <p class="tagline">D&amp;I Models, Assessments and Tools for You!</p>

</main>
</body>
</html>
```